Webdesign für ambulanter Pflegedienst
Zielgruppe
Es ist ein ambulanter Pflegedienst, der sich im Raum Dessau-Roßlau um die Versorgung sowie Betreuung von Menschen kümmert. Kontaktdaten: ambulanter Pflegedienst Hand Sorge; Inhaberin: Sabine Lohmar; Birkenweg 14, 06871 Dessau-Roßlau Telefon: 034907/519364
IK-Nummer: 47 283 6194
e-mail: sl-hand-sorge@postfeld.de
Aufgabenstellung
Die Farben sollen in Anlehnung an das Logo sein, dass mit übersandt wird.

```html
<!DOCTYPE html>
<html lang="de">
<head>
<meta charset="utf-8">
<title>Karriere – Hand Sorge</title>
<link href="https://fonts.googleapis.com/css2?family=Raleway:wght@400;500;600;700&family=Gloria+Hallelujah&display=swap" rel="stylesheet">
<style>
:root{
  --teal:#45aaa5;
  --teal-soft:#b3dcd8;
  --green:#7ab648;
  --sky:#dcedf7;
  --ink:#5e5e5e;
  --text:#707070;
  --line:#d9d9d9;
  --white:#fff;
}
*{box-sizing:border-box;margin:0;padding:0}
html,body{width:1200px;height:3561px;overflow:hidden;background:var(--white)}
body{font-family:'Raleway',sans-serif;color:var(--text)}
.page{position:relative;width:1200px;height:3561px;overflow:hidden}
.abs{position:absolute}
.script{font-family:'Gloria Hallelujah',cursive;color:var(--ink)}
.center{text-align:center;left:0;width:1200px}

/* nav */
.nav{top:0;left:0;width:1200px;height:50px}
.brand{left:250px;top:12px;display:flex;align-items:center;gap:6px;font-size:11px;font-weight:600;color:var(--teal)}
.brand i{width:16px;height:16px;border-radius:50%;border:2px solid var(--teal);display:block}
.nav a{position:absolute;top:17px;font-size:13px;color:var(--text);text-decoration:none}
.nav a.active{color:var(--green);font-weight:700}
.crumb{top:50px;left:0;width:1200px;height:26px;background:var(--sky);font-size:10px;text-align:center;line-height:26px;color:var(--teal)}
.crumb span{font-family:'Gloria Hallelujah',cursive;color:var(--ink);font-size:9px}

/* hero */
.hero{top:76px;left:0;width:1200px;height:180px;background:linear-gradient(90deg,var(--teal-soft) 0%,#d6ecea 45%,#fff 70%)}
.hero-photo{top:76px;left:827px;width:373px;height:180px;background:linear-gradient(120deg,#e9e2d8,#d7c6b1 50%,#b6a89a)}
.hero .kicker{position:absolute;left:263px;top:55px;font-size:15px}
.hero h1{position:absolute;left:263px;top:80px;font-size:30px;font-weight:600;color:var(--ink)}
.hero-badge{left:713px;top:174px;width:144px;height:144px;border-radius:50%;background:#fff;box-shadow:0 4px 14px rgba(0,0,0,.12);display:flex;align-items:center;justify-content:center}

/* section headings */
.sub{font-size:14px}
.h2{font-size:28px;font-weight:600;color:var(--ink);line-height:1.15}
.h2 em{font-style:normal;color:var(--teal)}
.rule{left:551px;width:98px;height:3px;background:var(--green)}
.lead{left:350px;width:500px;font-size:12.3px;line-height:1.3;text-align:center}
.lead p+p{margin-top:16px}

/* benefit cards */
.card{background:#fff;border:1px solid #eee;box-shadow:0 2px 8px rgba(0,0,0,.1);border-radius:4px;text-align:center;padding:0 26px}
.card h3{font-family:'Gloria Hallelujah',cursive;font-weight:400;font-size:14px;color:var(--ink);margin-top:62px;margin-bottom:18px}
.card p{font-size:12.3px;line-height:1.55}
.icon-dot{width:86px;height:86px;border-radius:50%;background:linear-gradient(180deg,#eef7f5,#b9dfda);display:flex;align-items:center;justify-content:center}

/* checklist */
.panel{background:#fff;box-shadow:0 2px 10px rgba(0,0,0,.12)}
.panel-head{height:58px;background:var(--sky);font-family:'Gloria Hallelujah',cursive;color:var(--ink);font-size:15px;line-height:58px;padding-left:30px}
.check{width:300px}
.check svg{position:absolute;left:-36px;top:-6px}
.check h4{font-size:14.5px;font-weight:700;color:var(--ink);margin-bottom:14px}
.check p{font-size:12px;line-height:1.3}

/* form */
.form-head{text-align:center;padding-left:0}
.label{font-size:12px;color:var(--ink)}
.field{border:1px solid #cfcfcf;border-radius:6px;background:#fff}
.drop{border:1px dashed var(--teal);background:#eaf5f5;border-radius:3px;text-align:center;font-size:10px;color:var(--ink)}
.drop a{color:var(--teal);text-decoration:underline}
.file{font-size:10px;color:var(--green);text-decoration:underline;display:flex;gap:6px;align-items:center}
.consent{font-size:9.5px;line-height:1.4;color:var(--text)}
.consent a{color:var(--teal);text-decoration:none}
.btn{background:var(--teal);color:#fff;border-radius:22px;font-size:12px;font-weight:700;display:flex;align-items:center;justify-content:center}

/* footer */
.footer{top:3279px;left:0;width:1200px;height:234px;background:linear-gradient(90deg,var(--teal-soft) 0%,#d2ebe8 40%,#e8ddd3 65%,#c9a98c 100%)}
.footer .script{position:absolute;left:263px;top:38px;font-size:18px}
.footer address{position:absolute;left:263px;top:70px;font-style:normal;font-size:12.5px;line-height:1.5;color:var(--ink)}
.footer-brand{position:absolute;left:500px;top:110px;width:200px;text-align:center;font-size:16px;font-weight:600;color:var(--ink);display:flex;gap:8px;justify-content:center;align-items:center}
.footer-brand i{width:14px;height:14px;border-radius:50%;background:var(--teal);display:block}
.to-top{left:833px;top:3245px;width:104px;height:104px;border-radius:50%;background:var(--sky);text-align:center;font-family:'Gloria Hallelujah',cursive;font-size:12px;color:var(--ink)}
.bottom{top:3513px;left:0;width:1200px;height:48px;background:var(--sky)}
.bottom a{position:absolute;top:18px;font-size:10px;font-weight:700;color:var(--ink);text-decoration:none;letter-spacing:.3px}
.bottom small{position:absolute;left:708px;top:19px;font-size:9px;color:var(--text)}
</style>
</head>
<body>
<div class="page">

  <nav class="abs nav">
    <div class="abs brand"><i></i>HAND SORGE</div>
    <a style="left:419px" href="#">Startseite</a>
    <a style="left:505px" href="#">Sofortige Hilfen</a>
    <a style="left:623px" href="#">Unsere Leistungen</a>
    <a class="active" style="left:760px" href="#">Karriere</a>
    <a style="left:834px" href="#">Pflegekurse</a>
  </nav>
  <div class="abs crumb">Hand Sorge - <span>Pflege von Mensch zu Mensch</span></div>

  <header class="abs hero">
    <div class="script kicker">Wir suchen Dich!</div>
    <h1>Karriere bei uns</h1>
  </header>
  <div class="abs hero-photo" role="img" aria-label="Foto: Pflegerin kümmert sich lächelnd um einen älteren Herrn"></div>
  <div class="abs hero-badge">
    <svg width="76" height="56" viewBox="0 0 76 56" fill="none" stroke="#555" stroke-width="2.5"><rect x="2" y="12" width="72" height="42" rx="4"/><path d="M26 12V5h24v7M2 28h30M44 28h30"/><rect x="32" y="23" width="12" height="11" rx="1"/></svg>
  </div>

  <div class="abs center script sub" style="top:360px">Pflege mit Herz &amp; Seele</div>
  <div class="abs center h2" style="top:392px">Komm in unser <em>Hand Sorge</em></div>
  <div class="abs rule" style="top:446px"></div>
  <div class="abs lead" style="top:476px">
    <p>Gehörst du zu den Menschen, die mit Herz und Seele Anderen zur Seite steht, unterstützt und versorgt, dann bist du hier genau richtig. Hilf uns die Pflege in der Umgebung Dessau-Roßlau qualitativ zu verbessern und menschlicher zu gestalten.</p>
    <p>Wir wissen, dass zufriedene Mitarbeiter bessere Arbeit leisten. Dies kommt nicht nur unseren Patienten zugute, sondern auch dem Teamgeist. Daher möchten wir ein Paar Goodies auflisten, die Mitarbeiter bei uns erhalten.</p>
  </div>

  <!-- benefit cards -->
  <div class="abs card" style="left:285px;top:676px;width:304px;height:307px">
    <h3>Urlaub</h3>
    <p>Bei uns erhält jeder Mitarbeiter 30 Tage Urlaub. Da wir wissen, wie wichtig Erholung ist. Weiterhin nehmen wir Rücksicht auf die individuelle Situation eines Mitarbeiters und versuchen die Dienstplan- und Tourengestaltung demnach anzupassen.</p>
  </div>
  <div class="abs icon-dot" style="left:394px;top:627px">
    <svg width="34" height="30" viewBox="0 0 34 30" fill="none" stroke="#555" stroke-width="1.5"><path d="M2 12a11 11 0 0 1 22 0zM13 12v14M2 27h30M24 5l3 2 3-2"/></svg>
  </div>

  <div class="abs card" style="left:608px;top:676px;width:304px;height:188px">
    <h3>Sonderleistungen</h3>
    <p>Weitere Sonderleistungen sind möglich. Sprich einfach mit uns und wir werden eine geeignete Lösung zusammen finden.</p>
  </div>
  <div class="abs icon-dot" style="left:717px;top:627px">
    <svg width="28" height="32" viewBox="0 0 28 32" fill="none" stroke="#555" stroke-width="1.5"><path d="M3 2h16l6 6v22H3z"/><path d="M8 12h12M8 17h12M8 22h7M20 24v6M17 27h6"/></svg>
  </div>

  <div class="abs card" style="left:608px;top:929px;width:304px;height:304px">
    <h3>Fort- &amp; Weiterbildungen</h3>
    <p>Finden interne und externe Fort- und Weiterbildungen statt, die bei voller Kostenübernahme, nach den individuellen Wünschen der Mitarbeiter ausgerichtet wird. Wir bilden dich gern zur Fachkraft aus. Egal welche Weiterbildung du machen möchtest wir stehen dir bei und werden dafür Sorge tragen, dass sie positiv beendet wird.</p>
  </div>
  <div class="abs icon-dot" style="left:717px;top:879px">
    <svg width="34" height="26" viewBox="0 0 34 26" fill="none" stroke="#555" stroke-width="1.5"><path d="M17 5C12 2 6 2 2 3v19c4-1 10-1 15 2 5-3 11-3 15-2V3c-4-1-10-1-15 2zM17 5v19M6 9h7M6 13h7M21 9h7M21 13h7"/></svg>
  </div>

  <div class="abs card" style="left:285px;top:1048px;width:304px;height:185px">
    <h3>Überdurchschnittliche Vergütung</h3>
    <p>Bei uns erhaltet ihr einen Zuschlag an Sonn- und Feiertagen von 100%.</p>
  </div>
  <div class="abs icon-dot" style="left:394px;top:997px">
    <svg width="30" height="30" viewBox="0 0 30 30" fill="none" stroke="#333" stroke-width="1.8"><rect x="3" y="8" width="24" height="19" rx="3"/><path d="M8 8l10-5 3 5M19 15h8v6h-8z"/></svg>
  </div>

  <div class="abs center script sub" style="top:1300px">Wir zählen auf Dich</div>
  <div class="abs center h2" style="top:1325px">Was wird auf Dich<br>zukommen?</div>
  <div class="abs rule" style="top:1412px"></div>
  <div class="abs lead" style="top:1437px">
    <p>Die ambulante Pflege wird in der Häuslichkeit der Patienten durchgeführt. Es ist unser Ziel die Pflege für alle Beteiligten so würdevoll und respektvoll zu gestalten wie möglich. Der zu betreuende Mensch steht dabei im Vordergrund, daher gewähren wir jedem die Zeit, die er braucht. Eine funktionierende Zusammenarbeit unter den Mitarbeitern ist uns genauso wichtig. Daher haben wir immer ein offenes Ohr für Patienten, Mitarbeiter und Angehöriger gleichermaßen.</p>
  </div>

  <!-- checklist -->
  <section class="abs panel" style="left:263px;top:1594px;width:673px;height:536px">
    <div class="panel-head">Deine Checkliste, das bringst Du mit</div>
  </section>
  <div class="abs check" style="left:336px;top:1679px;width:252px">
    <svg width="28" height="26" viewBox="0 0 28 26" fill="none"><rect x="1" y="5" width="20" height="20" rx="2" stroke="#45aaa5" stroke-width="2"/><path d="M6 14l5 6L26 2" stroke="#45aaa5" stroke-width="3.5" stroke-linecap="round"/></svg>
    <h4>Teamfähigkeit</h4>
    <p>Unser Hauptaugenmerk liegt auf der Teamfähigkeit. Dies bedeutet nicht nur unter den Mitarbeitern, sondern gegenüber den Angehörigen, den Patienten sowie anderen Professionen. Dabei ist uns ein harmonisches Miteinander sehr wichtig.</p>
  </div>
  <div class="abs check" style="left:336px;top:1833px;width:240px">
    <svg width="28" height="26" viewBox="0 0 28 26" fill="none"><rect x="1" y="5" width="20" height="20" rx="2" stroke="#45aaa5" stroke-width="2"/><path d="M6 14l5 6L26 2" stroke="#45aaa5" stroke-width="3.5" stroke-linecap="round"/></svg>
    <h4>Hilfsbereitschaft</h4>
    <p>Sind zur Teamfähigkeit ist die Hilfsbereitschaft sehr wichtig. Wir unterstützen uns alle gegenseitig und Sorgen auf diese Weise für ein gutes Betriebsklima.</p>
  </div>
  <div class="abs check" style="left:336px;top:1984px;width:245px">
    <svg width="28" height="26" viewBox="0 0 28 26" fill="none"><rect x="1" y="5" width="20" height="20" rx="2" stroke="#45aaa5" stroke-width="2"/><path d="M6 14l5 6L26 2" stroke="#45aaa5" stroke-width="3.5" stroke-linecap="round"/></svg>
    <h4>Gute Deutschkenntnisse</h4>
    <p>…in Wort und Schrift sind erforderlich, um sich mit den Patienten unterhalten zu können und der Dokumentationspflicht in Schriftform nachzukommen.</p>
  </div>
  <div class="abs check" style="left:646px;top:1679px;width:255px">
    <svg width="28" height="26" viewBox="0 0 28 26" fill="none"><rect x="1" y="5" width="20" height="20" rx="2" stroke="#45aaa5" stroke-width="2"/><path d="M6 14l5 6L26 2" stroke="#45aaa5" stroke-width="3.5" stroke-linecap="round"/></svg>
    <h4>Engagement</h4>
    <p>Egal ob du Quereinsteiger bist oder bereits Erfahrung im Pflegeberuf sammeln konntest, wenn du bereit bist deinen Wissensschatz stetig zu erweitern, bist du bei uns genau richtig. Wir sind der Meinung, dass niemand alles wissen kann, wenn jedoch die Bereitschaft zum Lernen besteht, ist das die halbe Miete. Wichtig ist, dass die Einstellung stimmt, den Rest bringen wir dir bei.</p>
  </div>
  <div class="abs check" style="left:646px;top:1907px;width:255px">
    <svg width="28" height="26" viewBox="0 0 28 26" fill="none"><rect x="1" y="5" width="20" height="20" rx="2" stroke="#45aaa5" stroke-width="2"/><path d="M6 14l5 6L26 2" stroke="#45aaa5" stroke-width="3.5" stroke-linecap="round"/></svg>
    <h4>Führerschein der Klasse B</h4>
    <p>Du bekommst von uns ein Auto gestellt, damit du zu den Patienten fahren kannst. Sollte keinen Führerschein vorhanden sein, stellen wir ein E-bike zur Verfügung und achten bei der Tourenplangestaltung auf die Distanz zum Patienten.</p>
  </div>

  <div class="abs center h2" style="top:2203px">Noch Fragen?</div>
  <div class="abs rule" style="top:2254px"></div>
  <div class="abs lead" style="top:2278px;left:400px;width:400px">
    <p>Dann sprich mit uns und wir werden diese bei einem gemeinsamen Treffen zusammen klären. Du kannst dich über folgendes Formular direkt bei uns bewerben. Wir melden uns auf jeden Fall bei dir.</p>
  </div>

  <!-- application form -->
  <section class="abs panel" style="left:332px;top:2407px;width:524px;height:773px">
    <div class="panel-head form-head" style="height:52px;line-height:52px">Bewirb Dich direkt online!</div>
  </section>
  <div class="abs label" style="left:370px;top:2493px">Nachname*</div>
  <div class="abs label" style="left:608px;top:2493px">Vorname*</div>
  <div class="abs field" style="left:370px;top:2516px;width:223px;height:38px"></div>
  <div class="abs field" style="left:608px;top:2516px;width:223px;height:38px"></div>
  <div class="abs label" style="left:370px;top:2569px">E-Mail*</div>
  <div class="abs label" style="left:641px;top:2569px">Telefonnummer*</div>
  <div class="abs field" style="left:370px;top:2592px;width:255px;height:39px"></div>
  <div class="abs field" style="left:641px;top:2592px;width:190px;height:39px"></div>
  <div class="abs label" style="left:370px;top:2646px">Möchtest Du noch etwas zu Deiner Bewerbung sagen?</div>
  <div class="abs field" style="left:370px;top:2668px;width:461px;height:83px"></div>
  <div class="abs label" style="left:370px;top:2767px">Anlagen beifügen</div>
  <div class="abs consent" style="left:370px;top:2794px;width:461px">Ziehe per Drag &amp; Drop deine Bewerbungsunterlagen in das Fenster oder klicke auf „Computer durchsuchen“. Wir wünschen uns von Dir ein Anschreiben, Lebenslauf, (xxxx).</div>
  <div class="abs drop" style="left:370px;top:2836px;width:461px;height:106px;padding-top:32px">
    Datei hier hinziehen<br><span style="font-size:7px">oder</span><br><a href="#">Computer durchsuchen</a>
  </div>
  <div class="abs label" style="left:370px;top:2958px">Deine Anlagen</div>
  <div class="abs file" style="left:370px;top:2983px">Lebenslauf_062023_maria-mustermann.pdf <svg width="9" height="11" viewBox="0 0 9 11" fill="none" stroke="#888"><path d="M1 3h7M3 3V1h3v2M2 3l.5 7h4L7 3"/></svg></div>
  <div class="abs file" style="left:370px;top:3003px">Anschreiben_062023_maria-mustermann.pdf <svg width="9" height="11" viewBox="0 0 9 11" fill="none" stroke="#888"><path d="M1 3h7M3 3V1h3v2M2 3l.5 7h4L7 3"/></svg></div>
  <div class="abs field" style="left:370px;top:3053px;width:29px;height:27px;border-radius:4px"></div>
  <div class="abs consent" style="left:410px;top:3050px;width:420px">Du erklärst Dich damit einverstanden, dass Deine Daten zur Bearbeitung Deiner Bewerbung verwendet werden. Weitere Informationen und Widerrufshinweise findest Du in der <a href="#">Datenschutzerklärung</a>.</div>
  <div class="abs btn" style="left:673px;top:3116px;width:153px;height:44px">Abenden</div>

  <!-- footer -->
  <footer class="abs footer">
    <div class="script">Wir sind für Sie da!</div>
    <address>ambulanter Pflegedienst Hand Sorge<br>Inhaberin: Sabine Lohmar<br>Birkenweg 14<br>06871 Dessau-Roßlau<br><span style="display:block;margin-top:8px">034907/519364</span>sl-hand-sorge@postfeld.de</address>
    <div class="footer-brand"><i></i>HAND SORGE</div>
    <div role="img" aria-label="Foto: ineinander gelegte Hände als Zeichen der Fürsorge" style="position:absolute;left:780px;top:0;width:420px;height:234px;background:linear-gradient(90deg,rgba(232,221,211,0),rgba(201,169,140,.6))"></div>
  </footer>
  <div class="abs to-top">
    <svg width="18" height="28" viewBox="0 0 18 28" style="margin-top:20px"><path d="M9 2v26M2 12l7-10 7 10" fill="#45aaa5" stroke="#45aaa5" stroke-width="3"/></svg>
    <div>Nach oben</div>
  </div>
  <div class="abs bottom">
    <a style="left:275px" href="#">KARRIERE</a>
    <a style="left:370px" href="#">KONTAKT</a>
    <a style="left:470px" href="#">DATENSCHUTZ</a>
    <a style="left:597px" href="#">IMPRESSUM</a>
    <small>Copyright 2023 © ambulanter Pflegedienst Hand Sorge</small>
  </div>
</div>
</body>
</html>
```